Off Campus Housing website service for universities needs corporate brochure

We need a corporate brochure targeted at universities to get them to partner with us to offer an Off-Campus Housing website with housing listings and educational resources for their students. We provide hosted software and support, off-campus housing listings, and educational resources to embed in the university website (i.e http://rentalhub.brx.edu); the university promotes the service to off-campus students, parents, and faculty/staff. We have a dedicated account executive to work with each university to promote the website to property managers in the schools area who pay to list their properties on the site. We currently partner with over 100 colleges and universities across the country to serve the needs of their off-campus students. Our corporate website is: www.lodgebridgealliance.com.
Updates

Target Market(s)

Universities and Colleges

Industry/Entity Type

Marketing

Font styles to use
Serif

Requirements
Must have
• Our logo
• Our website (www.lodgebridgealliance.com)
• Contact information (this is different than what we used on our previous brochure, image attached):
• Email: sales@lodgebridgealliance.com
• Student image(s) - must be diverse
• Phone: 866-402-7719
Nice to have
• University/Campus image (generic)

```html
<!DOCTYPE html>
<html lang="en">
<head>
<meta charset="utf-8">
<title>Lodgebridge Alliance – Brochure Spread</title>
<link rel="stylesheet" href="https://fonts.googleapis.com/css2?family=Lato:wght@400;700&family=Libre+Baskerville:wght@400&family=Oswald:wght@300;400;600&display=swap">
<style>
  :root {
    --brand-blue: #0b59bd;
    --brand-blue-deep: #084aa3;
    --ink-gray: #4a4a4c;
    --paper: #ffffff;
    --canvas: #e7e8ec;
    --tab-gray: #a9abb0;
    --photo-sky: #5f8fd0;
    --photo-stone: #e9e6df;
    --photo-warm: #d99a5a;
    --photo-cool: #9db6d6;
  }
  * { margin: 0; padding: 0; box-sizing: border-box; }
  html, body { width: 1200px; height: 1200px; overflow: hidden; }
  body { background: var(--canvas); position: relative; font-family: "Lato", sans-serif; }

  .spread {
    position: absolute; left: 39px; top: 163px;
    width: 1122px; height: 873px;
    display: flex;
  }
  .page { position: relative; width: 561px; height: 873px; overflow: hidden; }

  /* Back cover */
  .back-cover { background: var(--brand-blue); color: var(--paper); }
  .back-cover__photo {
    position: absolute; inset: 0;
    background: linear-gradient(160deg, rgba(255,255,255,0.10) 0%, rgba(255,255,255,0.03) 45%, rgba(0,20,70,0.18) 100%);
  }
  .contact { position: absolute; left: 0; right: 0; top: 388px; text-align: center; }
  .contact__title { font-weight: 700; font-size: 22px; letter-spacing: 0.5px; }
  .contact__company { font-size: 21px; margin-top: 8px; }
  .contact__details {
    position: absolute; top: 474px; left: 86px;
    display: flex; gap: 54px; font-size: 15.5px; line-height: 22.5px;
  }
  .contact__list { list-style: none; }
  .contact__line { display: flex; align-items: center; gap: 6px; }
  .contact__line svg { width: 13px; height: 13px; fill: var(--paper); flex: none; }
  .contact__address { display: grid; grid-template-columns: 13px auto; column-gap: 2px; }
  .contact__address svg { width: 10px; height: 13px; fill: var(--paper); margin-top: 5px; }

  .back-cover__tab {
    position: absolute; left: 33px; top: 800px; width: 485px; height: 90px;
    background: var(--paper); border-radius: 40px 40px 0 0;
  }
  .back-cover__wings { position: absolute; left: 72px; top: 790px; width: 410px; height: 12px; }
  .back-cover__logo {
    position: absolute; left: 145px; top: 770px; width: 275px; height: 70px;
    background: var(--paper); border: 2px solid var(--brand-blue);
    display: flex; align-items: center; justify-content: center;
  }

  .wordmark {
    font-family: "Libre Baskerville", serif; font-weight: 400;
    color: var(--brand-blue); text-align: center; text-transform: uppercase;
    line-height: 1.35;
  }
  .back-cover__logo .wordmark { font-size: 19px; letter-spacing: 5px; }

  /* Front cover */
  .front-cover { background: var(--paper); box-shadow: inset 14px 0 18px -12px rgba(0,0,0,0.18); }
  .front-cover__logo {
    position: absolute; left: 104px; top: 66px; width: 350px; height: 96px;
    border: 2px solid var(--brand-blue);
    display: flex; align-items: center; justify-content: center;
  }
  .front-cover__logo .wordmark { font-size: 25px; letter-spacing: 6px; }

  .photo { position: absolute; top: 205px; height: 369px; }
  .photo--campus { left: 26px; width: 248px;
    background: linear-gradient(180deg, var(--photo-sky) 0%, var(--photo-stone) 45%, #d8d4cb 80%, #6f8a3a 100%); }
  .photo--student { left: 295px; width: 248px;
    background: linear-gradient(160deg, #e8e3dc 0%, var(--photo-warm) 45%, var(--photo-cool) 80%, #c9b9a6 100%); }
  .photo-divider { position: absolute; left: 283px; top: 205px; width: 4px; height: 369px; background: var(--brand-blue); }

  .headline { position: absolute; left: 0; right: 0; top: 602px; text-align: center; font-family: "Oswald", sans-serif; line-height: 1; }
  .headline__lead { display: block; color: var(--ink-gray); font-weight: 600; font-size: 54px; transform: scaleX(1.22); }
  .headline__middle { display: block; color: var(--brand-blue); font-weight: 400; font-size: 58px; margin-top: 2px; transform: scaleX(1.09); }
  .headline__tail { display: block; color: var(--brand-blue); font-weight: 300; font-size: 58px; margin-top: 0; transform: scaleX(1.01); }

  .web-bar {
    position: absolute; left: 90px; top: 798px; width: 386px; height: 31px;
    background: var(--brand-blue); color: var(--paper);
    font-family: "Lato", sans-serif; font-weight: 700; font-size: 15px; letter-spacing: 5.5px;
    display: flex; align-items: center; justify-content: center;
    padding-left: 5px;
  }
</style>
</head>
<body>
  <main class="spread">
    <section class="page back-cover">
      <div class="back-cover__photo" role="img" aria-label="Faint blue-tinted photo of a columned campus building"></div>

      <div class="contact">
        <h2 class="contact__title">CONTACT US</h2>
        <p class="contact__company">Lodgebridge Alliance, LLC</p>
      </div>

      <div class="contact__details">
        <ul class="contact__list">
          <li class="contact__line"><svg viewBox="0 0 24 24"><path d="M6.6 10.8a15 15 0 0 0 6.6 6.6l2.2-2.2c.3-.3.7-.4 1-.2 1.1.4 2.3.6 3.6.6.6 0 1 .4 1 1V20c0 .6-.4 1-1 1A17 17 0 0 1 3 4c0-.6.4-1 1-1h3.5c.6 0 1 .4 1 1 0 1.3.2 2.5.6 3.6.1.3 0 .7-.2 1z"/></svg>(866) 402-7719</li>
          <li class="contact__line"><svg viewBox="0 0 24 24"><path d="M6.6 10.8a15 15 0 0 0 6.6 6.6l2.2-2.2c.3-.3.7-.4 1-.2 1.1.4 2.3.6 3.6.6.6 0 1 .4 1 1V20c0 .6-.4 1-1 1A17 17 0 0 1 3 4c0-.6.4-1 1-1h3.5c.6 0 1 .4 1 1 0 1.3.2 2.5.6 3.6.1.3 0 .7-.2 1z"/></svg>(555) 210-4837</li>
          <li class="contact__line"><svg viewBox="0 0 24 24"><path d="M6 3h12v5H6z M3 9h18v9h-3v3H6v-3H3z M8 15v4h8v-4z"/></svg>(555) 210-4900</li>
        </ul>
        <div class="contact__address">
          <svg viewBox="0 0 10 14"><path d="M5 0a5 5 0 0 1 5 5c0 3.5-5 9-5 9S0 8.5 0 5a5 5 0 0 1 5-5zm0 3a2 2 0 1 0 0 4 2 2 0 0 0 0-4z"/></svg>
          <span>PO Box 3180,</span>
          <span></span><span>Brookhaven, VA 24090-3180</span>
          <span></span><span>sales@lodgebridgealliance.com</span>
        </div>
      </div>

      <svg class="back-cover__wings" viewBox="0 0 410 12" aria-hidden="true">
        <polygon points="0,0 75,0 75,12 10,12" fill="var(--tab-gray)"/>
        <polygon points="335,0 410,0 400,12 335,12" fill="var(--tab-gray)"/>
      </svg>
      <div class="back-cover__tab"></div>
      <div class="back-cover__logo"><p class="wordmark">Lodgebridge<br>Alliance</p></div>
    </section>

    <section class="page front-cover">
      <div class="front-cover__logo"><p class="wordmark">Lodgebridge<br>Alliance</p></div>

      <div class="photo photo--campus" role="img" aria-label="White columned campus building under a blue sky"></div>
      <div class="photo-divider"></div>
      <div class="photo photo--student" role="img" aria-label="Student sitting cross-legged with a laptop in a bright living room"></div>

      <h1 class="headline">
        <span class="headline__lead">SIMPLIFYING</span>
        <span class="headline__middle">THE OFF-CAMPUS</span>
        <span class="headline__tail">HOUSING EXPERIENCE</span>
      </h1>

      <div class="web-bar">www.lodgebridgealliance.com</div>
    </section>
  </main>
</body>
</html>
```